Marke für hochwertige Trauerartikel benötigt Briefpapier
Zielgruppe
Weidkorn ist eine Marke für hochwertige Trauerartikel. Zielgruppe sind Bestattungsunternehmen, die nachhaltig zufriedenen Kunden möchten.
Aufgabenstellung
Wir benötigen Briefpapier: Anschreiben, Rechnngsformular in Farbe und in schwarz weiß. Dazu Visitenkarten und ein gleicherscheinenden E-Mail Absender. Das Design sollte so klar wir möglich sein. Der Druck erfolgt auf recyceltem Papier.

```html
<!DOCTYPE html>
<html lang="de">
<head>
<meta charset="utf-8">
<title>Weidkorn – Visitenkarte</title>
<link rel="stylesheet" href="https://fonts.googleapis.com/css2?family=Open+Sans:wght@400;600&display=swap">
<style>
  :root {
    --bg: #e9e7e3;
    --paper: #ffffff;
    --ink: #3a3a3a;
    --ink-dark: #111111;
    --gold: #d4b24c;
    --card-black: #1c1c1c;
    --back-ink: #e6e6e6;
  }
  * { box-sizing: border-box; margin: 0; padding: 0; }
  html, body { width: 1200px; height: 900px; overflow: hidden; }
  body {
    background: var(--bg);
    font-family: "Open Sans", Arial, sans-serif;
    color: var(--ink);
    position: relative;
  }
  .card {
    position: absolute;
    left: 250px;
    width: 700px;
    height: 400px;
    box-shadow: 0 6px 18px rgba(0,0,0,.18);
  }
  .card--front { top: 35px; background: var(--paper); }
  .card--back  { top: 465px; background: var(--card-black); }

  .brand {
    position: absolute;
    left: 50px; top: 70px;
    display: flex; align-items: center; gap: 12px;
    font-size: 28px; font-weight: 600; color: var(--ink-dark);
    letter-spacing: .5px;
  }
  .brand__square { width: 14px; height: 14px; background: var(--gold); }

  .address {
    position: absolute; right: 50px;
    text-align: right; font-size: 18px; line-height: 1.3;
    letter-spacing: .6px; font-style: normal;
  }
  .address--main   { bottom: 200px; }
  .address--branch { top: 222px; }

  .divider {
    position: absolute; left: 50px; right: 50px; top: 208px;
    height: 2px; background: var(--gold);
  }

  .contact {
    position: absolute; left: 50px; top: 222px;
    font-size: 18px; line-height: 1.4; letter-spacing: .6px;
  }
  .contact__row { display: flex; align-items: center; gap: 12px; }
  .contact__icon { width: 15px; height: 15px; flex: none; }

  .back-brand {
    position: absolute; left: 50%; top: 50%;
    transform: translate(-50%, -50%);
    display: flex; align-items: center; gap: 14px;
    font-size: 32px; font-weight: 400; color: var(--back-ink);
    letter-spacing: 1px;
  }
  .back-brand__square { width: 16px; height: 16px; background: var(--gold); }
</style>
</head>
<body>

  <section class="card card--front" aria-label="Visitenkarte Vorderseite">
    <div class="brand">
      <span class="brand__square"></span>
      <span class="brand__name">Weidkorn</span>
    </div>

    <address class="address address--main">Chemin des Tilleuls 7B<br>2316 Champvent-les-Prés</address>

    <div class="divider"></div>

    <address class="address address--branch">Rue des Vergers 12<br>3958 Grangeval</address>

    <div class="contact">
      <div class="contact__row">
        <svg class="contact__icon" viewBox="0 0 16 16" aria-hidden="true">
          <path d="M3 1.5h3l1.2 3.3-1.8 1.2a9 9 0 0 0 4.6 4.6l1.2-1.8 3.3 1.2v3a1.5 1.5 0 0 1-1.6 1.5A13 13 0 0 1 1.5 3.1 1.5 1.5 0 0 1 3 1.5z" fill="var(--gold)"/>
        </svg>
        <span>078 315 40 22</span>
      </div>
      <div class="contact__row">
        <svg class="contact__icon" viewBox="0 0 16 16" aria-hidden="true">
          <rect x="1" y="3" width="14" height="10" rx="1.5" fill="var(--gold)"/>
          <path d="M1.8 4l6.2 4.8L14.2 4" fill="none" stroke="#fff" stroke-width="1.3"/>
        </svg>
        <span>info@weidkorn-probe.ch</span>
      </div>
      <div class="contact__row">
        <svg class="contact__icon" viewBox="0 0 16 16" aria-hidden="true">
          <circle cx="8" cy="8" r="7" fill="var(--gold)"/>
          <g fill="none" stroke="#fff" stroke-width="1">
            <ellipse cx="8" cy="8" rx="3" ry="6.5"/>
            <line x1="1.5" y1="8" x2="14.5" y2="8"/>
          </g>
        </svg>
        <span>www.weidkorn-probe.ch</span>
      </div>
    </div>
  </section>

  <section class="card card--back" aria-label="Visitenkarte Rückseite">
    <div class="back-brand">
      <span class="back-brand__square"></span>
      <span class="back-brand__name">Weidkorn</span>
    </div>
  </section>

</body>
</html>
```